UL Aesthetic improvement on full website

marbleferngo.com
We need someone to improve the current website marbleferngo.com
Some designed to fail to follow isntruction and deliver. please find attached summary latest design requirement, please follow and read each of the requirements carefully and submit max two versions only. The winner would have to deliver within 5 days

Sample reference : pelorix.com/html/marblefern/#
(previous winner cant deliver)
*All of our wording and graphic content are updated, designer wouldn't involve in recreating any content.
Designer may use template or own material. delivery in html and implement on our WordPress server

please submit about us the project submission.
upon the winning, you have to maintain sub content / pages and submit the full site with your improved version of full websites including inner pages

Low design quality

Target Market(s)

general audience

Industry/Entity Type

social service

Number of Pages Required

5+ page

Requirements
Must have
• feeling and look similar to quenvo dot com
Nice to have
• extend the same style to other pages

```html
<!DOCTYPE html>
<html lang="en">
<head>
<meta charset="utf-8">
<title>Marble Fern — Social Inclusion</title>
<link href="https://fonts.googleapis.com/css2?family=Montserrat:wght@400;500;600;700;800&display=swap" rel="stylesheet">
<style>
:root{
  --coral:#f86b6b;
  --coral-soft:#fcb9bb;
  --blush:#fff4f4;
  --ink:#111111;
  --text:#333333;
  --muted:#6b6b6b;
  --white:#ffffff;
  --line:#e6e6e6;
}
*{margin:0;padding:0;box-sizing:border-box}
html,body{width:958px;height:1200px;overflow:hidden}
body{font-family:'Montserrat',sans-serif;background:var(--white);position:relative;color:var(--text)}
.abs{position:absolute}
.page-tint{left:0;top:640px;width:958px;height:560px;background:linear-gradient(var(--white),var(--blush) 20%,var(--white) 60%)}

.brand-badge{border-radius:50%;background:var(--coral);color:var(--white);font-weight:700;display:flex;align-items:center;justify-content:center;text-align:center;letter-spacing:1px;line-height:1.1}
.site-header .brand-badge{left:70px;top:10px;width:42px;height:42px;font-size:6.5px}
.main-nav{left:358px;top:23px;display:flex;font-size:9.5px;font-weight:500;color:var(--ink);letter-spacing:.3px}
.main-nav a{position:absolute;white-space:nowrap;color:inherit;text-decoration:none}
.main-nav a.active{color:var(--coral)}
.main-nav a.active::after{content:"";position:absolute;left:0;bottom:-3px;width:12px;height:1px;background:var(--coral)}
.login-btn{left:795px;top:16px;width:93px;height:29px;border-radius:15px;background:var(--coral);color:var(--white);font-size:10.5px;font-weight:600;display:flex;align-items:center;justify-content:center;gap:5px}

.hero-kicker{left:71px;top:162px;font-size:20px;color:var(--ink)}
.hero-title{left:68px;top:182px;font-size:70px;font-weight:700;color:var(--coral);line-height:70px;letter-spacing:-.5px}
.store-btn{top:370px;width:162px;height:43px;border-radius:22px;background:var(--white);box-shadow:0 2px 10px rgba(248,107,107,.25);display:flex;align-items:center;gap:10px;padding-left:30px}
.store-btn .mark{width:22px;height:22px;border-radius:4px;background:var(--coral)}
.store-btn small{display:block;font-size:6px;color:var(--ink);text-transform:uppercase}
.store-btn strong{display:block;font-size:12.5px;font-weight:500;color:var(--ink)}

.hero-art{left:482px;top:100px}
.partners-title{left:0;width:958px;top:550px;text-align:center;color:var(--coral);font-size:17px;font-weight:600}
.partner-row{left:115px;top:606px;width:730px;display:flex;justify-content:space-between;align-items:center}
.partner{font-size:13px;font-weight:700;color:#3a2a6b;display:flex;align-items:center;gap:6px;white-space:nowrap}
.partner i{width:14px;height:14px;background:var(--coral);display:inline-block}
.carousel-arrow{top:612px;width:16px;height:16px;border-radius:50%;border:1.5px solid var(--muted);display:flex;align-items:center;justify-content:center;font-size:9px;color:var(--muted);line-height:1}
.carousel-arrow.next{border-color:var(--coral);color:var(--coral)}

.newsletter-band{left:0;top:725px}
.newsletter-title{left:71px;top:814px;font-size:21px;font-weight:700;color:var(--ink)}
.newsletter-copy{left:71px;top:850px;width:380px;font-size:12px;line-height:16.5px;color:var(--ink)}
.field{top:801px;width:186px;height:34px;border-radius:17px;background:var(--white);font-size:10.5px;color:#999;padding-left:19px;display:flex;align-items:center}
.consent{left:514px;top:848px;display:flex;align-items:center;gap:7px;font-size:10.5px;color:var(--ink)}
.consent span{width:15px;height:15px;border-radius:3px;background:var(--white)}
.subscribe-btn{left:504px;top:879px;width:127px;height:31px;border-radius:16px;background:var(--coral);color:var(--white);font-size:11.5px;font-weight:600;display:flex;align-items:center;justify-content:center}

.site-footer .brand-badge{left:70px;top:1012px;width:46px;height:46px;font-size:7px}
.footer-heading{color:var(--coral);font-size:15px;font-weight:600}
.footer-about{left:148px;top:1035px;font-size:10px;line-height:15px;color:var(--ink)}
.social{top:1095px;width:31px;height:31px;border-radius:50%;border:1.5px solid var(--coral);color:var(--coral);font-size:6.5px;font-weight:600;display:flex;align-items:center;justify-content:center}
.footer-links{list-style:none;font-size:10.5px;color:var(--muted)}
.footer-links li{height:20px;line-height:20px}
.footer-links li.active{color:var(--coral);text-decoration:underline}
.footer-rule{left:70px;top:1163px;width:818px;height:1px;background:var(--line)}
.copyright{left:0;width:958px;top:1176px;text-align:center;font-size:10px;color:var(--muted)}
</style>
</head>
<body>
<div class="abs page-tint"></div>

<header class="site-header">
  <div class="abs brand-badge">MARBLE<br>FERN</div>
  <nav class="abs main-nav">
    <a class="active" style="left:0">HOME</a>
    <a style="left:60px">ABOUT US</a>
    <a style="left:141px">OUR STORY</a>
    <a style="left:228px">SOCIAL IMPACT</a>
    <a style="left:335px">JOIN US</a>
  </nav>
  <div class="abs login-btn">
    <svg width="8" height="9" viewBox="0 0 8 9"><circle cx="4" cy="2.3" r="2.1" fill="#fff"/><path d="M0 9c0-3 1.8-4 4-4s4 1 4 4z" fill="#fff"/></svg>Login
  </div>
</header>

<section class="hero">
  <p class="abs hero-kicker">New way of giving</p>
  <h1 class="abs hero-title">Social<br>Inclusion</h1>
  <div class="abs store-btn" style="left:70px"><span class="mark"></span><div><small>Get it on</small><strong>Playstand</strong></div></div>
  <div class="abs store-btn" style="left:245px"><span class="mark"></span><div><small>Download on the</small><strong>Orchard Store</strong></div></div>
  <svg class="abs hero-art" width="400" height="360" viewBox="0 0 400 360">
    <path d="M30 70 C90 50 160 70 210 60 C280 45 320 20 360 35 C410 55 400 160 350 220 C290 290 210 355 120 356 C50 357 0 300 0 220 C0 140 -10 85 30 70Z" fill="var(--coral-soft)"/>
    <g role="img" aria-label="Two phones showing the Marble Fern app: a food merchant menu and a browse screen with featured merchants">
      <rect x="172" y="1" width="145" height="296" rx="18" fill="#1e1e1e"/>
      <rect x="176" y="5" width="137" height="288" rx="15" fill="#fff3e0"/>
      <rect x="85" y="41" width="147" height="299" rx="18" fill="#1e1e1e"/>
      <rect x="89" y="45" width="139" height="291" rx="15" fill="#ffe3e3"/>
    </g>
  </svg>
</section>

<section class="partners">
  <h2 class="abs partners-title">Partners</h2>
  <div class="abs carousel-arrow" style="left:70px">&#8592;</div>
  <div class="abs partner-row">
    <span class="partner"><i></i>Civic Media Board</span>
    <span class="partner">Westbay Polytechnic</span>
    <span class="partner" style="color:#1aa851">Ridora</span>
    <span class="partner"><i></i>Corvan Bank</span>
    <span class="partner" style="color:#1b2450">Halvern Capital</span>
  </div>
  <div class="abs carousel-arrow next" style="left:869px">&#8594;</div>
</section>

<section class="newsletter">
  <svg class="abs newsletter-band" width="958" height="245" viewBox="0 0 958 245">
    <path d="M0 24 C120 -4 240 0 360 12 C520 28 650 8 760 10 C860 12 920 0 958 10 L958 230 C860 250 760 232 620 218 C480 204 360 218 240 228 C120 238 40 224 0 212Z" fill="var(--coral-soft)"/>
  </svg>
  <h2 class="abs newsletter-title">SUBSCRIBE TO OUR NEWSLETTER</h2>
  <p class="abs newsletter-copy">Let’s stay in touch! We would like to keep you inspired with our Kindness stories and community events.</p>
  <div class="abs field" style="left:504px">First Name</div>
  <div class="abs field" style="left:702px">Email</div>
  <label class="abs consent"><span></span>By continuing, you accept the privacy policy</label>
  <div class="abs subscribe-btn">SUBSCRIBE</div>
</section>

<footer class="site-footer">
  <div class="abs brand-badge">MARBLE<br>FERN</div>
  <h3 class="abs footer-heading" style="left:147px;top:1004px">Follow us and stay updated!</h3>
  <p class="abs footer-about">A Singapore Social Enterprise.<br>In a world where you can be anything, be kind.</p>
  <div class="abs social" style="left:148px">Facet</div>
  <div class="abs social" style="left:187px">Lensly</div>
  <div class="abs social" style="left:226px">Streamo</div>
  <div class="abs social" style="left:265px">Wirely</div>

  <h3 class="abs footer-heading" style="left:551px;top:1005px">Quick Link</h3>
  <ul class="abs footer-links" style="left:551px;top:1030px">
    <li class="active">Home</li><li>About Us</li><li>Our Story</li><li>Social Impact</li><li>Marble Fern</li>
  </ul>
  <h3 class="abs footer-heading" style="left:741px;top:1006px">Links</h3>
  <ul class="abs footer-links" style="left:741px;top:1031px">
    <li>Fern Business</li><li>Merchant</li><li>The Fern Gift</li><li>FAQs</li><li>Contact Us</li>
  </ul>
  <div class="abs footer-rule"></div>
  <p class="abs copyright">COPYRIGHT © 2021 MARBLE FERN SINGAPORE</p>
</footer>
</body>
</html>
```